Modes of Action Brochure/Handout

We need an innovative, professional design for a multi page presentation of our research findings. We want a clean, fresh layout, want to utilize a couple photos we have bought and included in the example we put together for a starting point.. We want it to read easily.

Target Market(s)

Dietary Supplement Industry

Industry/Entity Type

It Professional

Requirements
Must have
• Attention getting, attractive.

```html
<!DOCTYPE html>
<html lang="en">
<head>
<meta charset="UTF-8">
<title>VitaCore – Modes of Action Brochure</title>
<link rel="stylesheet" href="https://fonts.googleapis.com/css2?family=Montserrat:wght@400;600;700&family=Open+Sans:wght@400;600&display=swap">
<style>
  :root {
    --backdrop: #e4e8e8;
    --paper: #ffffff;
    --paper-shade: #f2f3f3;
    --teal: #2fa69c;
    --teal-dark: #1f7f78;
    --gold: #c9a94b;
    --ink: #3f5a58;
    --photo-family: #b9b2a8;
    --photo-cells: #8a2a25;
    --photo-outdoor: #7fa65a;
  }
  * { box-sizing: border-box; margin: 0; padding: 0; }
  html, body { width: 1200px; height: 900px; overflow: hidden; }
  body {
    background: var(--backdrop);
    font-family: "Open Sans", Arial, sans-serif;
    position: relative;
  }
  .page {
    position: absolute;
    top: 195px;
    width: 360px;
    height: 510px;
    background: linear-gradient(180deg, var(--paper) 0%, var(--paper-shade) 100%);
    box-shadow: 0 6px 18px rgba(0,0,0,0.12);
    overflow: hidden;
  }
  .cover { left: 40px; }
  .spread-left { left: 440px; }
  .spread-right { left: 800px; box-shadow: 6px 6px 18px rgba(0,0,0,0.12); }
  .spread-left::after {
    content: ""; position: absolute; right: 0; top: 0; width: 24px; height: 100%;
    background: linear-gradient(90deg, rgba(0,0,0,0) 0%, rgba(0,0,0,0.08) 100%);
  }
  .circle { position: absolute; border-radius: 50%; }
  .ring-teal { border: 3px solid var(--teal); background: transparent; }
  .ring-gold { border: 3px solid var(--gold); background: transparent; }

  /* Cover */
  .cover-title-disc {
    left: 75px; top: 25px; width: 210px; height: 210px;
    background: var(--gold);
    display: flex; flex-direction: column; align-items: center; justify-content: center;
    text-align: center; color: #fff; font-family: "Montserrat", Arial, sans-serif;
  }
  .cover-title-disc .kicker { font-size: 12px; font-weight: 400; letter-spacing: 0.5px; line-height: 1.25; }
  .cover-title-disc .headline { font-size: 30px; font-weight: 700; letter-spacing: 0.5px; line-height: 1.05; }
  .cover-title-disc .joiner { font-size: 9px; font-weight: 600; }
  .cover-title-disc .subline { font-size: 18px; font-weight: 700; }
  .cover-ring { left: 90px; top: 200px; width: 180px; height: 180px; }
  .cover-photo {
    left: 100px; top: 210px; width: 160px; height: 160px;
    background: radial-gradient(circle at 50% 40%, #e2ddd5 0%, var(--photo-family) 70%, #8e877e 100%);
  }
  .brand {
    position: absolute; left: 30px; bottom: 35px;
    border-left: 2px solid var(--gold); padding-left: 10px;
  }
  .brand-name {
    font-family: "Montserrat", Arial, sans-serif; font-weight: 600; font-size: 20px; color: var(--gold);
  }
  .brand-tagline {
    font-family: "Montserrat", Arial, sans-serif; font-size: 7px; letter-spacing: 1.5px; color: var(--gold);
  }

  /* Spread left */
  .intro-disc {
    left: 10px; top: 10px; width: 250px; height: 250px; background: var(--teal);
    display: flex; align-items: center; justify-content: center; padding: 40px;
    color: #fff; font-size: 9.5px; line-height: 1.55; text-align: center;
  }
  .accent-disc { left: 205px; top: 225px; width: 90px; height: 90px; background: var(--gold); }
  .cells-ring { left: -20px; top: 315px; width: 215px; height: 215px; }
  .cells-photo {
    left: -8px; top: 327px; width: 191px; height: 191px;
    background: radial-gradient(circle at 55% 45%, #c7402f 0%, var(--photo-cells) 60%, #4a1512 100%);
  }
  .side-note {
    position: absolute; left: 222px; top: 350px; width: 115px;
    font-size: 8.5px; line-height: 1.5; color: var(--teal-dark);
  }

  /* Spread right */
  .outdoor-ring { left: 170px; top: -25px; width: 205px; height: 205px; }
  .outdoor-photo {
    left: 180px; top: -15px; width: 185px; height: 185px;
    background: radial-gradient(circle at 45% 50%, #d8d2c6 0%, var(--photo-outdoor) 65%, #4e7436 100%);
  }
  .summary-disc {
    left: 10px; top: 55px; width: 120px; height: 120px; background: var(--teal);
    display: flex; align-items: center; justify-content: center; text-align: center;
    font-family: "Montserrat", Arial, sans-serif; font-weight: 600; font-size: 15px;
    line-height: 1.2; color: var(--gold);
  }
  .body-column {
    position: absolute; width: 150px;
    font-size: 9px; line-height: 1.75; color: var(--ink); text-align: justify;
  }
  .body-column.first { left: 22px; top: 200px; }
  .body-column.second { left: 188px; top: 200px; }
</style>
</head>
<body>

<section class="page cover">
  <div class="circle cover-title-disc">
    <span class="kicker">HIGH PRIORITY<br>SUPPORT FOR</span>
    <span class="headline">IMMUNITY</span>
    <span class="joiner">AND</span>
    <span class="subline">GOOD HEALTH</span>
  </div>
  <div class="circle cover-ring ring-teal"></div>
  <div class="circle cover-photo" role="img" aria-label="Photo of a smiling family of four"></div>
  <div class="brand">
    <div class="brand-name">VitaCore</div>
    <div class="brand-tagline">MODES OF ACTION</div>
  </div>
</section>

<section class="page spread-left">
  <div class="circle intro-disc">
    <p>Our research team reviewed more than ten years of clinical data to understand how targeted nutrients support the body's natural defences. This handout summarises the key findings, the modes of action we identified and what they mean for daily wellness and good health.</p>
  </div>
  <div class="circle accent-disc"></div>
  <div class="circle cells-ring ring-gold"></div>
  <div class="circle cells-photo" role="img" aria-label="Microscopic illustration of blood and immune cells"></div>
  <p class="side-note">Specific nutrients help regulate immune cell activity, balance inflammatory response and protect tissues from everyday oxidative stress.</p>
</section>

<section class="page spread-right">
  <div class="circle outdoor-ring ring-teal"></div>
  <div class="circle outdoor-photo" role="img" aria-label="Photo of a woman outdoors holding a drink after exercise"></div>
  <div class="circle summary-disc">Executive<br>Summary</div>
  <p class="body-column first">A healthy immune system depends on steady nutrition, restful sleep and balanced daily habits. Our review focused on compounds that show measurable effects in controlled studies and that can be combined safely in a single formula. Each ingredient was assessed for quality, purity and consistency before it was considered for inclusion. We also compared dosage ranges, absorption rates and long term tolerance across different age groups, so that the final recommendations reflect real daily use rather than short laboratory trials alone.</p>
  <p class="body-column second">The findings point to several modes of action working together. Some nutrients strengthen the first line of defence, while others help the body recover and maintain balance over time. Antioxidant compounds protect cells from daily stress, and selected minerals support normal enzyme activity. Together they offer practical support for immunity and long term good health. The sections that follow describe each mode of action in detail, the evidence behind it and how it fits into a simple routine that people can follow every day.</p>
</section>

</body>
</html>
```